Flyer für Alltagsbegleitung
Zielgruppe
Firma: Tageshilfe am Fluss
Meine Zielgruppe sind alle Menschen, die im Alltag, Hilfe benötigen.
Aufgabenstellung
Der Flyer soll modern und und ansprechend aussehen. Es soll vermerkt sein, das ich als annerkannte Kraft, Entlastungsleistung nach

```html
<!DOCTYPE html>
<html lang="de">
<head>
<meta charset="utf-8">
<title>Tageshilfe am Fluss – Flyer</title>
<link href="https://fonts.googleapis.com/css2?family=Barlow+Condensed:wght@600&family=Lexend:wght@500;600&display=swap" rel="stylesheet">
<style>
:root{
  --stage:#4a4a4a;
  --green:#68a934;
  --green-dark:#4f8f2a;
  --green-light:#b7d88c;
  --green-pale:#dfe8ac;
  --ink:#1f4a2a;
  --white:#ffffff;
}
*{margin:0;padding:0;box-sizing:border-box}
html,body{width:1200px;height:838px;overflow:hidden;background:var(--stage)}
body{position:relative;font-family:'Lexend',sans-serif;color:var(--ink)}
.page{position:absolute;top:33px;width:544px;height:772px;overflow:hidden}
.front{left:38px;background:linear-gradient(180deg,var(--green-light) 0%,#9ccb6a 55%,var(--green) 100%)}
.back{left:627px;background:linear-gradient(180deg,var(--green) 0%,#a6cf7c 45%,#d9e4c8 60%)}
.abs{position:absolute}
.top-band{left:0;top:0;width:100%;height:15px;background:var(--green)}
.title{left:0;width:100%;top:36px;text-align:center;font-family:'Barlow Condensed',sans-serif;font-weight:600;font-size:66px;line-height:74px;color:var(--ink)}
.photo{border-radius:50%;border:10px solid var(--green-dark)}
.photo-a{left:21px;top:185px;width:240px;height:240px;background:radial-gradient(circle at 40% 40%,#e6eef2,#9fb2bf)}
.photo-b{left:273px;top:260px;width:256px;height:256px;background:radial-gradient(circle at 55% 45%,#eceff0,#b59a72)}
.waves{left:0;top:430px}
.question{left:35px;top:526px;font-size:24.5px;line-height:30px;font-weight:600;color:var(--white)}
.footer-band{left:0;top:594px;width:100%;height:178px;background:var(--green-pale)}
.legal{left:0;width:100%;top:624px;text-align:center;font-size:18.5px;line-height:21px;font-weight:600;color:var(--ink)}
.legal .hl{color:var(--green)}
.phone-pill{left:152px;top:707px;width:242px;height:32px;border-radius:16px;background:var(--green-light);display:flex;align-items:center;gap:18px;padding-left:6px;font-size:22px;font-weight:600;letter-spacing:2px}
.phone-dot{width:24px;height:24px;border-radius:50%;background:var(--green-dark);display:flex;align-items:center;justify-content:center}
.heading-pill{left:108px;top:30px;width:328px;height:40px;border-radius:20px;background:var(--green-light);text-align:center;font-size:23px;font-weight:600;line-height:40px}
.service{width:180px;text-align:center;font-size:15.5px;line-height:15px;font-weight:600}
.icon{width:54px;height:54px;border-radius:50%;background:var(--white);margin:0 auto 8px;display:flex;align-items:center;justify-content:center}
.section-title{left:0;width:100%;top:356px;text-align:center;font-size:28px;font-weight:600}
.rule{top:375px;width:54px;height:2px;background:var(--ink)}
.intro{left:0;width:100%;top:403px;text-align:center;font-size:19.5px;line-height:23px;font-weight:600}
.hands{left:0;top:440px;width:100%;height:230px;background:linear-gradient(100deg,#e9e6df 0%,#d9b49a 45%,#e3d7cc 80%,#f1f1f1 100%)}
.contact-pill{left:36px;top:640px;width:292px;height:44px;border-radius:22px;background:var(--green-light);padding:3px 0 0 21px;font-size:17px;line-height:19px;font-weight:600}
.contact{color:var(--white);font-size:19px;line-height:26px;font-weight:600;letter-spacing:1px}
.divider{left:161px;top:697px;width:3px;height:45px;background:var(--white)}
</style>
</head>
<body>

<section class="page front">
  <div class="abs top-band"></div>
  <h1 class="abs title">Tageshilfe<br>am Fluss</h1>
  <div class="abs photo photo-a" role="img" aria-label="Foto: Betreuungskraft hält die Hände einer älteren Dame"></div>
  <svg class="abs waves" width="544" height="170" viewBox="0 0 544 170" aria-hidden="true">
    <path d="M0 22 C150 15 260 60 340 105 C420 145 480 160 544 165 L544 170 L0 170 Z" fill="var(--green)"/>
    <path d="M0 6 C150 5 260 60 340 105 C420 145 480 155 544 155" fill="none" stroke="var(--green-light)" stroke-width="3"/>
  </svg>
  <div class="abs photo photo-b" role="img" aria-label="Foto: lächelnde Betreuerin mit älterem Herrn im Sessel"></div>
  <p class="abs question">Sie wünschen sich<br>Unterstützung im Alltag?</p>
  <div class="abs footer-band"></div>
  <p class="abs legal">Anerkannte Betreuungskraft gemäß <span class="hl">§ 45b SGB XI</span><br><span class="hl">Entlastungsleistungen</span> können direkt<br>mit der Pflegekasse abgerechnet werden.</p>
  <div class="abs phone-pill">
    <span class="phone-dot"><svg width="13" height="13" viewBox="0 0 24 24"><path fill="#fff" d="M6.6 10.8a15 15 0 0 0 6.6 6.6l2.2-2.2c.3-.3.7-.4 1-.2 1.1.4 2.3.6 3.6.6.6 0 1 .4 1 1V20c0 .6-.4 1-1 1A17 17 0 0 1 3 4c0-.6.4-1 1-1h3.5c.6 0 1 .4 1 1 0 1.3.2 2.5.6 3.6.1.3 0 .7-.2 1z"/></svg></span>
    0170 4582 336
  </div>
</section>

<section class="page back">
  <div class="abs heading-pill">Unsere Dienstleistungen</div>

  <div class="abs service" style="left:54px;top:91px">
    <div class="icon"><svg width="30" height="30" viewBox="0 0 24 24" fill="none" stroke="var(--green-dark)" stroke-width="2"><path d="M3 11l9-7 9 7M5 10v10h14V10"/></svg></div>
    Hilfe im Haushalt<br>&amp; beim Einkaufen
  </div>
  <div class="abs service" style="left:229px;top:91px">
    <div class="icon"><svg width="30" height="30" viewBox="0 0 24 24" fill="var(--green-dark)"><path d="M12 20s-7-4.5-7-10a4 4 0 0 1 7-2.5A4 4 0 0 1 19 10c0 5.5-7 10-7 10z"/></svg></div>
    Arzt -<br>&amp; Freizeitbegleitung
  </div>
  <div class="abs service" style="left:388px;top:91px">
    <div class="icon"><svg width="30" height="30" viewBox="0 0 24 24" fill="none" stroke="var(--green-dark)" stroke-width="2"><path d="M4 4h16v10H9l-5 4z"/></svg></div>
    Gesellschaft<br>&amp; Gespräche
  </div>
  <div class="abs service" style="left:124px;top:207px">
    <div class="icon"><svg width="30" height="30" viewBox="0 0 24 24" fill="none" stroke="var(--green-dark)" stroke-width="2"><path d="M3 9h18l-2 10H5zM8 9l3-5M16 9l-3-5"/></svg></div>
    Einkäufe<br>und Spaziergänge
  </div>
  <div class="abs service" style="left:313px;top:207px">
    <div class="icon"><svg width="30" height="30" viewBox="0 0 24 24" fill="none" stroke="var(--green-dark)" stroke-width="2"><path d="M6 3h9l4 4v14H6zM9 11h7M9 15h7"/></svg></div>
    Hilfe bei Anträgen<br>&amp; Formularen
  </div>

  <div class="abs hands" role="img" aria-label="Foto: junge Hände halten die Hand eines älteren Menschen"></div>
  <div class="abs rule" style="left:70px"></div>
  <h2 class="abs section-title">Betreuungsdienst</h2>
  <div class="abs rule" style="left:420px"></div>
  <p class="abs intro">Als erfahrene und engagierte Betreuungskraft<br>unterstütze ich Sie persönlich dabei, Ihren Alltag<br>angenehmer und strukturierter zu gestalten.</p>

  <svg class="abs" style="left:0;top:560px" width="544" height="212" viewBox="0 0 544 212" aria-hidden="true">
    <path d="M0 67 C200 45 400 25 544 16 L544 212 L0 212 Z" fill="var(--green)"/>
    <path d="M0 67 C200 45 400 25 544 16" fill="none" stroke="var(--green-light)" stroke-width="6"/>
  </svg>
  <div class="abs contact-pill">Kontaktieren Sie mich für ein<br>kostenloses Erstgespräch</div>
  <p class="abs contact" style="left:60px;top:694px">Olga<br>Lupen</p>
  <div class="abs divider"></div>
  <p class="abs contact" style="left:190px;top:694px">0170 4582 336<br>olga.lupen@postmail.de</p>
</section>

</body>
</html>
```